Family Psychologist Needs a Sign Designed - Logo Supplied

I am looking for signage on the front window that is bright and catches people’s eyes as they drive past. Therefore, the writing can’t be too small that it is too hard to focus on and read from a moving car.

I want to maybe incorporate the floating spots somehow. I am also looking to hang a banner over the side of the front railing that lists what services are offered since the name doesn’t exactly cover it all . Services include: Psychology, Speech, OT. There is also an education component to the business where we do Study Skills Coaching to high school kids. I would like to see an option of this incorporated to but in a separate way so it isn’t associated with the “psychology” part of the business as this may deter people.

I also want to put a sign above the business in the overhead light thing (not sure what its called). Currently it is empty but the clinics next door have “chiropractor” and “medical centre” written in theirs so mine will have to be as equally simple but specific. Logo attached (EPS)

Ive also attached my logo and a few examples of where the signagewill go.

```html
<!DOCTYPE html>
<html lang="en">
<head>
<meta charset="utf-8">
<title>Bright Steps — Multiclinic &amp; Education Sign</title>
<link rel="stylesheet" href="https://fonts.googleapis.com/css2?family=Arimo:wght@700&display=swap">
<style>
  :root {
    --frame: #363435;
    --panel-edge: #e4f3ee;
    --panel-mid: #f8fbe9;
    --panel-glow: #fdfef6;
    --ink-dark: #414042;
    --teal: #45bccb;
    --brand-teal: #4bb6b4;
    --brand-green: #8cc63f;
  }
  * { margin: 0; padding: 0; box-sizing: border-box; }
  html, body {
    width: 1200px;
    height: 1026px;
    overflow: hidden;
    background: var(--frame);
  }
  .sign {
    position: relative;
    width: 1200px;
    height: 1026px;
    background: var(--frame);
    font-family: "Arimo", Arial, sans-serif;
  }
  .sign__panel {
    position: absolute;
    left: 88px;
    top: 86px;
    width: 1024px;
    height: 854px;
    background:
      radial-gradient(ellipse 420px 380px at 512px 300px, var(--panel-glow) 0%, rgba(253,254,246,0) 100%),
      linear-gradient(90deg, var(--panel-edge) 0%, var(--panel-mid) 35%, var(--panel-mid) 65%, var(--panel-edge) 100%);
  }
  .brand {
    position: absolute;
    left: 255px;
    top: 262px;
    display: flex;
    align-items: center;
    gap: 28px;
  }
  .brand__square {
    width: 340px;
    height: 340px;
    background: var(--brand-green);
  }
  .brand__name {
    color: var(--brand-teal);
    font-size: 104px;
    font-weight: 700;
    line-height: 1.05;
    letter-spacing: 1px;
  }
  .tagline {
    position: absolute;
    left: 0;
    width: 1200px;
    text-align: center;
    font-weight: 700;
  }
  .tagline--clinic {
    top: 660px;
    font-size: 62px;
    color: var(--ink-dark);
  }
  .tagline--services {
    top: 748px;
    font-size: 54px;
    color: var(--teal);
  }
</style>
</head>
<body>
  <div class="sign">
    <div class="sign__panel" role="img" aria-label="Soft pale green and cream background with floating white spots"></div>

    <div class="brand">
      <div class="brand__square"></div>
      <div class="brand__name">BRIGHT<br>STEPS</div>
    </div>

    <p class="tagline tagline--clinic">Multiclinic &amp; Education</p>
    <p class="tagline tagline--services">OT | Speech | Psychology</p>
  </div>
</body>
</html>
```